Cover-Design für Buchprojekt
kiwano suchte ein neues Design in der Kategorie Buch-/eBook-Cover und hat ein Projekt auf entwurfsbuero.de gestartet.
Das sagt der Auftraggeber
Vielen Dank für das wunderbare, moderne Design unseres Buchcovers. Ihre Freundlichkeit, Schnelligkeit und Geduld bei der Ausarbeitung war sehr professionell. Wir empfehlen Sie gerne weiter und speichern Ihr Profil für das nächste Projekt. kiwano
Zielgruppe
Wir benötigen ein Cover für ein Buchprojekt, in dem es um Geld sparen für Kinder in Aktien/ETFs geht.
Eltern/Großeltern/Onkel/Tanten möchten Geld ansparen für ihr Kind, wissen aber, dass ein Sparbuch heutzutage aufgrund der niedrigen Zinsen keine gute Möglichkeit ist, haben schon von ETFs gehört (oder legen selber an) und möchten nun auch ein Depot für ihr Kind (Enkelkind, Nichte, Neffe) anlegen.
Zielgruppe:
1. Eltern (eher Mütter), die sich bereits selbst mit dem Thema Geldanlage beschäftigt haben, die selbst bereits ein ETF-Depot zur Altersvorsorge haben und nun überlegen, wie sie für ihr Kind/Kinder diese Vorteile auch nutzen können.
2 Eltern, bei denen Verwandte (Großeltern/Tanten/Onkel) den Wunsch haben, für die Kinder Geld anzusparen für die Zukunft. Doch diese möchten in einen Aktienfonds bei der Bank investieren, die Eltern kennen sich mit modernen Formen der Geldanlage aus und finden es sinnvoller, einen ETF-Depot fürs Kind einzurichten. Nun möchten sie die Verwandten mit diesem Buch davon überzeugen.
- Welche Probleme und Herausforderungen hat diese Zielgruppe?
Sie sind finanziell recht stabil aufgestellt und machen sich nun Gedanken um die Zukunft ihrer Kinder. Als Sicherheit möchten sie auch für ihre Kinder sparen. Sei es, um später mal ein Studium/Ausbildung zu finanzieren (eine „gute“ Ausbildung, womöglich auch ein Auslandssemester zu ermöglichen), den Führerschein, die erste eigene Wohnung oder einfach nur als Finanzpolster, wenn mal „was passiert“.
- Welche Ziele verfolgt deine Zielgruppe?
Sie möchten Sicherheit und Wohlstand für ihre Kinder/Enkel.
Sie möchten trotz Niedrigzinsumfeld das Geld fürs Kind sicher und gewinnbringend in ETFs anlegen.
Aufgabenstellung
Hochwertiges, modernes, minimalistisches Design, das sich von der Masse abhebt. Keine Aktiencharts. Keine Pflanzen, die wachsen oder gegossen werden. Gerne ein Design, das Sicherheit fürs Kind vermittelt (kein Muss). Keine Personen frontal. Wirkung wie ein seriöser Ratgeber (z.B. wie Ratgeber vom RT Verlag oder PW).
Autor: Konstantin Brugger
Titel/Untertitel: Unser Nachwuchs baut früh Vermögen auf. Wie Eltern sicher in ETFs sparen, Fallstricke von Anfang an vermeiden und ein Geld-Mindset prägen
Backcover und Buchrücken wird benötigt (dies erst im nächsten Schritt, Backcovertext wird dann gegeben)
Format Taschenbuch: 5x8

```html
<!DOCTYPE html>
<html lang="de">
<head>
<meta charset="utf-8">
<title>GELD 2021 – Buchcover</title>
<link rel="stylesheet" href="https://fonts.googleapis.com/css2?family=Abel&family=Roboto:wght@700&display=swap">
<style>
  :root {
    --page-bg: #e4e4e4;
    --cover-navy: #1d3344;
    --text-light: #eef1f4;
    --ring-rose: #9c3a78;
  }
  * { margin: 0; padding: 0; box-sizing: border-box; }
  html, body {
    width: 1200px;
    height: 848px;
    overflow: hidden;
    background: var(--page-bg);
  }
  .stage {
    width: 1200px;
    height: 848px;
    display: flex;
    align-items: center;
    justify-content: center;
  }
  .book-cover {
    position: relative;
    width: 475px;
    height: 760px;
    background: var(--cover-navy);
    color: var(--text-light);
  }
  .title-mark {
    position: absolute;
    left: 0;
    top: 0;
    width: 475px;
    height: 360px;
  }
  .subtitle {
    position: absolute;
    left: 0;
    right: 0;
    top: 398px;
    text-align: center;
    font-family: "Abel", sans-serif;
    font-size: 24px;
    line-height: 1.2;
    letter-spacing: 0.2px;
  }
  .author {
    position: absolute;
    left: 0;
    right: 0;
    top: 700px;
    text-align: center;
    font-family: "Abel", sans-serif;
    font-size: 17px;
    letter-spacing: 3px;
  }
</style>
</head>
<body>
<main class="stage">
  <article class="book-cover">
    <svg class="title-mark" viewBox="0 0 475 360" aria-labelledby="cover-title">
      <title id="cover-title">GELD 2021</title>
      <defs>
        <radialGradient id="ring-glow" cx="50%" cy="50%" r="50%">
          <stop offset="0%" stop-color="var(--ring-rose)" stop-opacity="0.04"/>
          <stop offset="85%" stop-color="var(--ring-rose)" stop-opacity="0.2"/>
          <stop offset="100%" stop-color="var(--ring-rose)" stop-opacity="0"/>
        </radialGradient>
      </defs>
      <circle class="ring-field" cx="226" cy="205" r="118" fill="url(#ring-glow)"
              role="img" aria-label="Feine konzentrische Linienkreise in Rosé hinter dem Titel"/>
      <text class="title-word" x="226" y="252" text-anchor="middle"
            font-family="'Abel', sans-serif" font-size="160"
            fill="var(--text-light)">GELD</text>
      <text class="title-year" x="352" y="306" text-anchor="end"
            font-family="'Roboto', sans-serif" font-weight="700" font-size="42"
            fill="var(--text-light)">2021</text>
    </svg>
    <p class="subtitle">Für Kinder<br>Geld sicher, gewinnbringend und<br>smart anlegen</p>
    <p class="author">BUCHAUTOR</p>
  </article>
</main>
</body>
</html>
```